Webdesign für die Veranstaltungsreihe Wolkenreigen
Zielgruppe
Für die Veranstaltungsreihe 'Wolkenreigen' soll ein Website-Design entwickelt werden, welches potentielle Besucher über die Veranstaltung informiert (Standorte, Anfahrt, Preise etc.) und gleichzeitig eine Foto- bzw. Videodokumentation der vergangenen 'Wolkenreigen' bietet.
Zielgruppe:
Personen jeder Altersgruppe, Gruppen wie (Familien, Vereine etc.)
Aufgabenstellung
Das Design sollte...
einfach und modern
nicht zu verspielt
freundlich
kreativ
innovativ
den Inhalt der Veranstaltungsreihe
...wiederspiegeln.
Bitte orientieren Sie sich an dem bestehenden Design der Eventreihe.

```html
<!DOCTYPE html>
<html lang="de">
<head>
<meta charset="utf-8">
<title>Wolkenreigen – Der Wettstreit der Pyrotechniker</title>
<link href="https://fonts.googleapis.com/css2?family=Open+Sans:wght@300;400;600;700&display=swap" rel="stylesheet">
<style>
:root{
  --orange:#f39200;
  --gold:#f7c948;
  --ink:#333;
  --muted:#666;
  --light:#f6f6f6;
  --bar:#dcdcdc;
  --white:#fff;
  --black:#000;
}
*{box-sizing:border-box;margin:0;padding:0}
html,body{width:1135px;height:1200px;overflow:hidden;background:var(--white)}
body{font-family:"Open Sans",sans-serif;color:var(--ink);position:relative}
a{color:inherit}
.wrap{position:absolute;left:230px;width:677px}

.site-header{position:absolute;top:0;left:0;width:1135px;height:76px}
.brand{position:absolute;left:230px;top:0;width:178px;height:76px;background:var(--black);display:flex;align-items:center;justify-content:center;gap:7px}
.brand-dot{width:9px;height:9px;background:var(--orange)}
.brand-name{color:var(--orange);font-weight:700;font-size:16px;letter-spacing:.3px}
.main-nav{position:absolute;left:485px;top:0;height:76px;display:flex}
.main-nav a{display:flex;align-items:center;padding:0 6px;font-size:9.3px;text-decoration:none;letter-spacing:.1px;color:#222}
.main-nav a.active{background:#f2f2f2;font-weight:600;padding:0 5px 0 6px;width:61px}

.hero{position:absolute;top:76px;left:0;width:1135px;height:286px;
  background:linear-gradient(100deg,#c98a76 0%,#8c4f6c 25%,#6f3f66 50%,#5a4a72 75%,#b87f79 100%)}
.hero-text{position:absolute;left:248px;top:115px;color:var(--white)}
.hero-text h1{font-weight:400;font-size:15.5px;line-height:21px;letter-spacing:.1px}
.hero-links{margin-top:7px;display:flex;gap:15px;font-size:13px;color:var(--gold)}

.intro{top:400px}
.intro h2{color:var(--orange);font-weight:300;font-size:18.5px;line-height:22px;width:290px}
.intro p{font-size:9.7px;line-height:12px;width:318px;margin-top:22px}
.intro ul{list-style:none;font-size:9.7px;line-height:12px;margin-top:12px}
.video{position:absolute;left:337px;top:2px;width:339px;height:190px;background:radial-gradient(circle at 60% 35%,#3a1a08 0%,#0a0604 45%,#000 100%)}
.video-bar{position:absolute;left:5px;right:5px;bottom:15px;height:2px;background:#555}
.video-bar span{display:block;width:50%;height:2px;background:#e62117}

.events{position:absolute;top:631px;left:0;width:1135px;height:339px;background:var(--light)}
.events h2{position:absolute;top:30px;width:100%;text-align:center;font-weight:300;font-size:19px;color:#444}
.cards{position:absolute;left:230px;top:76px;display:flex;gap:11px}
.card{width:218px;height:219px;background:var(--white);position:relative}
.card-date{position:absolute;left:10px;top:10px;font-size:8.6px;color:var(--orange)}
.card-title{position:absolute;left:11px;top:23px;font-size:10.7px;font-weight:600}
.card-photo{position:absolute;left:0;top:49px;width:218px;height:105px}
.card-text{position:absolute;left:12px;top:164px;width:200px;font-size:8.2px;line-height:9.2px}
.card-info{position:absolute;left:12px;top:200px;font-size:10px}
.btn{position:absolute;right:0;bottom:0;width:92px;height:24px;background:var(--orange);color:var(--white);font-size:10px;font-weight:600;display:flex;align-items:center;justify-content:center;gap:5px}

.site-footer{position:absolute;top:1020px;left:0;width:1135px}
.col{position:absolute;top:0;font-size:8.3px;line-height:10.3px;color:var(--muted)}
.col h3{font-weight:400;font-size:8.8px;color:#333;margin-bottom:9px}
.col p{margin-bottom:10px}
.col ul{list-style:none;line-height:14px;margin-bottom:12px}
.legal{position:absolute;top:1175px;left:0;width:1135px;height:25px;background:var(--bar);font-size:8.5px;color:var(--muted)}
.legal nav{position:absolute;left:230px;top:7px;display:flex;gap:9px}
</style>
</head>
<body>

<header class="site-header">
  <div class="brand"><span class="brand-dot"></span><span class="brand-name">WOLKENREIGEN</span></div>
  <nav class="main-nav">
    <a class="active" href="#">STARTSEITE</a>
    <a href="#">WOLKENREIGEN</a>
    <a href="#">RAHMENPROGRAMM</a>
    <a href="#">VERANSTALTUNGEN</a>
    <a href="#">TICKETS &amp; PREISE</a>
  </nav>
</header>

<section class="hero" role="img" aria-label="Publikum in Silhouette vor einem farbigen Feuerwerkshimmel">
  <div class="hero-text">
    <h1>ERLEBEN SIE DEN WETTSTREIT DER PYROTECHNIKER<br>BEI DREI FANTASTISCHEN MUSIKFEUERWERKEN.</h1>
    <div class="hero-links"><span>» Braunschweig</span><span>» Padderborn</span><span>» Oberhausen</span></div>
  </div>
</section>

<section class="wrap intro">
  <h2>DAS FEUERWERKSPEKTAKEL FÜR DIE GANZE FAMILIE.</h2>
  <p>Drei renommierte Pyrotechniker treten beim Wolkenreigen gegeneinander an und versuchen, das Publikum und die Fachjury mit ihren <b>spektakulären Feuerwerks-Choreografien</b> zu überzeugen und den Siegerpokal für sich zu gewinnen. Ein <b>fantastisches Erlebnis</b> für die ganze Familie mit großem Rahmenprogramm und kulinarischem Angebot.</p>
  <ul>
    <li>› Fantastischen Musikfeuerwerke</li>
    <li>› Spektakuläre Feuerwerks-Choreografien</li>
    <li>› Rahmenprogramm für die ganze Familie</li>
    <li>› Großes kulinarisches Angebot</li>
  </ul>
  <div class="video" role="img" aria-label="Videoplayer mit Feuerwerks-Trailer">
    <div class="video-bar"><span></span></div>
  </div>
</section>

<section class="events">
  <h2>ERLEBEN SIE WOLKENREIGEN</h2>
  <div class="cards">
    <article class="card">
      <div class="card-date">18. Juni 2016</div>
      <div class="card-title">Wolkenreigen in Braunschweig</div>
      <div class="card-photo" role="img" aria-label="Beleuchtetes Schlossgebäude in der Dämmerung" style="background:linear-gradient(180deg,#4f7fb8 0%,#a9b9c7 60%,#8b7a5a 100%)"></div>
      <p class="card-text">At vero eos et accusam et justo duo dolores et ea rebum. Stet clita kasd gubergren, no sea takimata sanctus est Lorem ipsum dolor sit amet.</p>
      <a class="card-info">› <u>Informationen</u></a>
      <a class="btn"><svg width="9" height="8" viewBox="0 0 9 8"><path d="M0 0h2l1 5h5l1-4H3" fill="none" stroke="#fff" stroke-width="1.2"/><circle cx="3.5" cy="7" r="1" fill="#fff"/><circle cx="7.5" cy="7" r="1" fill="#fff"/></svg>Tickets kaufen</a>
    </article>
    <article class="card">
      <div class="card-date">18. Juni 2016</div>
      <div class="card-title">Wolkenreigen in Padderborn</div>
      <div class="card-photo" role="img" aria-label="Gelb angestrahltes Renaissanceschloss bei Nacht" style="background:linear-gradient(180deg,#1a1408 0%,#8a6a10 45%,#d6a915 70%,#2a1e06 100%)"></div>
      <p class="card-text">At vero eos et accusam et justo duo dolores et ea rebum. Stet clita kasd gubergren, no sea takimata sanctus est Lorem ipsum dolor sit amet.</p>
      <a class="card-info">› <u>Informationen</u></a>
      <a class="btn"><svg width="9" height="8" viewBox="0 0 9 8"><path d="M0 0h2l1 5h5l1-4H3" fill="none" stroke="#fff" stroke-width="1.2"/><circle cx="3.5" cy="7" r="1" fill="#fff"/><circle cx="7.5" cy="7" r="1" fill="#fff"/></svg>Tickets kaufen</a>
    </article>
    <article class="card">
      <div class="card-date">18. Juni 2016</div>
      <div class="card-title">Wolkenreigen in Oberhausen</div>
      <div class="card-photo" role="img" aria-label="Rot beleuchteter Industrieturm mit Lichterweg bei Nacht" style="background:radial-gradient(circle at 50% 35%,#8a3a22 0%,#3a2010 40%,#140c06 100%)"></div>
      <p class="card-text">At vero eos et accusam et justo duo dolores et ea rebum. Stet clita kasd gubergren, no sea takimata sanctus est Lorem ipsum dolor sit amet.</p>
      <a class="card-info">› <u>Informationen</u></a>
      <a class="btn"><svg width="9" height="8" viewBox="0 0 9 8"><path d="M0 0h2l1 5h5l1-4H3" fill="none" stroke="#fff" stroke-width="1.2"/><circle cx="3.5" cy="7" r="1" fill="#fff"/><circle cx="7.5" cy="7" r="1" fill="#fff"/></svg>Tickets kaufen</a>
    </article>
  </div>
</section>

<footer class="site-footer">
  <div class="col" style="left:230px;width:225px">
    <h3>WOLKENREIGEN - DER WETTSTREIT DER PYROTECHNIKER</h3>
    <p>Lorem ipsum dolor sit amet, consetetur sadipscing elitr, sed diam nonumy eirmod tempor invidunt ut labore et dolore magna aliquyam erat, sed diam voluptua.</p>
    <p>At vero eos et accusam. At justo duo dolores et ea rebum. Stet clita kasd gubergren, no sea takimata sanctus est Lorem ipsum dolor sit amet.</p>
    <p>› <u>mehr erfahren</u></p>
  </div>
  <div class="col" style="left:517px;width:200px">
    <h3>KARTEN BESTELLEN</h3>
    <ul>
      <li>› <u>Karten für Wolkenreigen in Braunschweig</u></li>
      <li>› <u>Karten für Wolkenreigen in Padderborn</u></li>
      <li>› <u>Karten für Wolkenreigen in Oberhausen</u></li>
    </ul>
    <h3>WEITERE INFORMATIONEN</h3>
    <ul>
      <li>› <u>Was ist Wolkenreigen</u></li>
      <li>› <u>Was Besucher über Wolkenreigen sagen</u></li>
    </ul>
  </div>
  <div class="col" style="left:747px;width:170px">
    <h3>KONTAKT</h3>
    <p>Lumora Events UG (haftungsbeschränkt)<br>Lindenweg 7b<br>45999 Musterstadt</p>
    <p>Telefon: (01 23) 456 78 900<br><u>kontakt@lumora-events.de</u><br><u>www.lumora-events.de</u></p>
  </div>
</footer>

<div class="legal">
  <nav><u>Impressum</u><u>AGB</u><u>Haftungsausschluss</u></nav>
</div>

</body>
</html>
```